Medical Centre Website

We need a new design for a medical centre based in Perth, Western Australia called 'Tarwick Valley Medical Centre'.

The medical centre does general practitioner work including general checkups, ecg, heart checks, woman's health and more servicing children and adults. They also do home visits on occasions where the patient cannot attend the centre.

They would like an information/brochure website where visitors can read up on the practice, send email and view their location.

The client wish the design to be clean, fresh and light. The main colours are a light purple/blue and to a dark navy blue. The client would not want the logo to be altered in any way. This includes changing the words colours or the image.

The final design should represent a loving, family friendly practice where patients can come to receive the best treatments.

We just need the end product to be presented to un in a layed psd format. The fonts must be as per the W3C standards.

**IMPORTANT**
I have received heaps of skype invites in the past. To treat everyone fairly, I do not add people to my skype list as in the past people expected us to give them the prize. If you have questions, please ask them in pixel forum as it may benefit others who are also designing the site. If I need to, I will send a message to the user.
Updates

Hi Designers,

Most designs we have received have been overly cluttered. Are you able to simplify the designs.

Cheers, Dorian

Hi Designers,

Some of the designs are quite attractive but aremore cluttered than I would like. If you have a look at the following design, the design is very simple and straight to the point. A lot of designs have too much wording and the reader can be put off. We are looking something more like:

fernoakclinic.com.au

I would prefer to see designs and have opened up the contest for a further 7 days.

Designers,

We have received feedback from the client and Quite frankly he don’t really like any of them.They are too cluttered and Americanised. All drab blue colours.
 
If you have a look at template monster, these designs are better and cleaner. We do not want heaps of writing on the front page.

If you look at the eariler examples such as kelbrookgp.com.au which I did myself, the client loves that simplicity of the site.

```html
<!DOCTYPE html>
<html lang="en">
<head>
<meta charset="utf-8">
<title>Tarwick Valley Medical Centre</title>
<link href="https://fonts.googleapis.com/css2?family=Ubuntu:wght@300;400;500&family=Arimo:wght@400;700&display=swap" rel="stylesheet">
<style>
:root{
  --page-bg:#e8e8e8;
  --sheet:#ffffff;
  --navy:#123a6e;
  --blue:#1a7fc4;
  --sky:#5fb8ec;
  --line:#c9c9c9;
  --panel-top:#ffffff;
  --panel-bottom:#e6e6e6;
  --text:#4a4a4a;
}
*{box-sizing:border-box;margin:0;padding:0}
html,body{width:1200px;height:1089px;overflow:hidden}
body{background:var(--page-bg);font-family:"Arimo",Arial,sans-serif;color:var(--text);position:relative}
.sheet{position:absolute;left:90px;top:0;width:1020px;height:1089px;background:var(--sheet);box-shadow:0 0 14px rgba(0,0,0,.12)}
.box{position:absolute;border:1px solid var(--line);border-radius:6px;background:linear-gradient(var(--panel-top),var(--panel-bottom))}
.site-header{left:100px;top:-6px;width:980px;height:120px}
.brand{position:absolute;left:24px;top:36px;display:flex;align-items:center;gap:14px}
.brand-name{font-family:"Ubuntu",sans-serif;font-weight:400;color:var(--navy);font-size:30px;line-height:1}
.brand-name small{display:block;font-size:17px;letter-spacing:3px;margin-top:6px}
.brand-mark{width:40px;height:40px;border-radius:50%;background:var(--sky);flex:none}
.tagline{position:absolute;right:30px;top:56px;font-family:"Ubuntu",sans-serif;font-size:27px;color:var(--navy);font-weight:400}
.tagline span{color:var(--blue)}
.main-nav{position:absolute;left:100px;top:119px;width:980px;height:44px;border-radius:4px;background:linear-gradient(#8fd0f6,#39a3e4 50%,#1d88d2);border:1px solid #1b78ba;display:flex}
.main-nav a{font-family:"Ubuntu",sans-serif;font-size:18px;color:#fff;text-decoration:none;display:flex;align-items:center;justify-content:center;border-right:1px solid rgba(20,90,150,.45);box-shadow:1px 0 0 rgba(255,255,255,.35)}
.main-nav a:last-child{border:0;box-shadow:none}
.main-nav a.current{color:var(--navy)}
.hero{position:absolute;left:100px;top:170px;width:980px;height:304px;border-radius:6px;border:1px solid var(--line);background:linear-gradient(#3d6c78,#7ea7ad 45%,#3b4a55 75%,#22282d)}
.feature{width:237px;height:204px;top:484px}
.feature h3,.side h3{height:37px;border-bottom:1px solid var(--line);font-family:"Ubuntu",sans-serif;font-weight:400;font-size:19px;color:var(--blue);padding:8px 0 0 9px;text-transform:uppercase}
.thumb{position:absolute;left:9px;top:46px;right:9px;height:114px;background:#fff;border:1px solid var(--line);border-radius:3px;padding:5px}
.thumb div{width:100%;height:100%}
.btn{position:absolute;font-family:"Arimo",sans-serif;font-weight:700;font-size:12px;color:#777;background:linear-gradient(#fff,#e4e4e4);border:1px solid #c3c3c3;border-radius:3px;display:flex;align-items:center;justify-content:center}
.feature .btn{left:9px;top:171px;width:84px;height:22px}
.feature .btn.active{color:var(--navy)}
.welcome{position:absolute;left:100px;top:706px;width:667px}
.welcome h1{font-family:"Ubuntu",sans-serif;font-weight:300;font-size:30px;color:var(--navy);margin-bottom:9px}
.welcome h1 span{color:var(--blue)}
.welcome p{font-size:14px;line-height:18px;text-align:justify;margin-bottom:18px}
.side{left:777px;width:303px}
.field{position:absolute;left:11px;width:275px;height:22px;border:1px solid #d0d0d0;border-radius:4px;background:#fff;box-shadow:inset 0 1px 2px rgba(0,0,0,.1);font-size:12px;color:#444;padding:3px 9px}
.side .btn{left:11px;top:108px;width:78px;height:22px;color:var(--navy)}
.ad{display:flex;align-items:center;justify-content:center;text-align:center;font-family:"Ubuntu",sans-serif;font-size:27px;line-height:31px;color:var(--blue)}
.site-footer{left:100px;top:975px;width:980px;height:77px}
.foot-nav{position:absolute;left:14px;top:30px;font-family:"Ubuntu",sans-serif;font-size:13px;color:#333}
.foot-nav a{color:#333;text-decoration:none}
.foot-nav a.current{color:var(--blue)}
.foot-nav i{font-style:normal;margin:0 8px}
.socials{position:absolute;right:10px;top:20px;display:flex;gap:10px}
.socials span{font-family:"Ubuntu",sans-serif;font-size:12px;color:var(--navy);height:36px;padding:0 8px;display:flex;align-items:center;border:1px solid var(--line);border-radius:5px;background:#fff}
.copyright{position:absolute;left:100px;top:1060px;font-size:12px;color:var(--blue);text-decoration:underline}
</style>
</head>
<body>
<div class="sheet"></div>

<header class="box site-header">
  <div class="brand">
    <div class="brand-name">Tarwick Valley<small>MEDICAL CENTRE</small></div>
    <div class="brand-mark"></div>
  </div>
  <div class="tagline"><span>caring for</span> EVERY FAMILY <span>in</span> THE VALLEY</div>
</header>

<nav class="main-nav">
  <a class="current" style="width:134px">Home</a>
  <a style="width:175px">About Us</a>
  <a style="width:166px">Services</a>
  <a style="width:176px">Locations</a>
  <a style="width:134px">FAQ</a>
  <a style="width:195px">Contact Us</a>
</nav>

<div class="hero" role="img" aria-label="Photo of the medical centre's glass entrance with a patient walking in"></div>

<section class="box feature" style="left:100px">
  <h3>Woman's Health</h3>
  <div class="thumb"><div role="img" aria-label="Photo of a female doctor with a family in a clinic" style="background:linear-gradient(#eef2f5,#d7e1e8)"></div></div>
  <a class="btn active">Read More</a>
</section>
<section class="box feature" style="left:347px">
  <h3>Heart Check</h3>
  <div class="thumb"><div role="img" aria-label="Photo of a stethoscope held to a patient's chest" style="background:linear-gradient(90deg,#8aa0c8,#6b7fb4)"></div></div>
  <a class="btn">Read More</a>
</section>
<section class="box feature" style="left:594px">
  <h3>Heading Here</h3>
  <div class="thumb"><div role="img" aria-label="Photo of a dental check-up" style="background:linear-gradient(#c9463f,#e0a49a)"></div></div>
  <a class="btn">Read More</a>
</section>
<section class="box feature" style="left:841px;width:239px">
  <h3>Heading Here</h3>
  <div class="thumb"><div role="img" aria-label="Photo of a doctor measuring a patient's blood pressure" style="background:linear-gradient(90deg,#e9eef1,#b7c0c7)"></div></div>
  <a class="btn">Read More</a>
</section>

<article class="welcome">
  <h1><span>Welcome to</span> Tarwick Valley</h1>
  <p>Lorem Ipsum is simply dummy text of the printing and typesetting industry. Lorem Ipsum has been the industry's standard dummy text ever since the 1500s, when an unknown printer took a galley of type and scrambled it to make a type specimen book. It has survived not only five centuries, but also the leap into electronic typesetting, remaining essentially unchanged. It was popularised in the 1960s with the release of Pressline sheets containing Lorem Ipsum passages, and more recently with desktop publishing software like Folio Layout including versions of Lorem Ipsum.</p>
  <p>Lorem Ipsum is simply dummy text of the printing and typesetting industry. Lorem Ipsum has been the industry's standard dummy text ever since the 1500s, when an unknown printer took a galley of type and scrambled it to make a type specimen book. It has survived not only five centuries, but also the leap into electronic typesetting, remaining essentially unchanged.</p>
</article>

<aside class="box side" style="top:698px;height:141px">
  <h3>User Login</h3>
  <div class="field" style="top:49px">user name:</div>
  <div class="field" style="top:77px">password:</div>
  <a class="btn">LOGIN</a>
</aside>

<aside class="box side ad" style="top:850px;height:115px">ADVERTISING<br>FOR TARWICK VALLEY</aside>

<footer class="box site-footer">
  <nav class="foot-nav">
    <a class="current">Home</a><i>|</i><a>About Us</a><i>|</i><a>Services</a><i>|</i><a>Locations</a><i>|</i><a>FAQ</a><i>|</i><a>Contact Us</a>
  </nav>
  <div class="socials"><span>Linkwall</span><span>Chirpline</span><span>Coinlane</span></div>
</footer>

<div class="copyright">Copyright © 2004-2015 Tarwick Valley Medical Centre, Inc. All Rights Reserved.</div>
</body>
</html>
```